2 page Web Site Design (Coded), simple, not picky

I need a web portal for a PPC marketing business. I have the logo, some imagery, and some websites to base the design on.

***Background***
The name of the business is "Quiet Harbor Outreach Partners" or QHOP. We provide listings in a searchable database for Dental Sleep Medicine doctors. These are doctors who treat snoring/sleep apnea/and CPAP users with oral appliances. Client doctors will have their own "landing page website" where PPC prospects land from the PPC campaigns. Logos for supporting/landing page websites have been uploaded.
***End Background***

THIS website (for you to design) is to introduce doctors to the concept and detail the services. i.e. PPC campaign management services, listing on a national database of Dental Sleep Medicine practitioners, and a fully featured website dedicated to Snoring, Sleep Apnea, and CPAP Alternative treatment (those websites are "Farewell-Rumble.com", "Farewell-NightPause.com", and ""Farewell-MaskFree.com")

SEM websites whose look I enjoy are:

http://www.brivolta.com/marketing-services/pay-per-click/

http://www.quellandrift.com/welcome/pay-per-click-services/

http://www.tarnolux4co.com/marketing-services/paid-search-management/

The main colors are Red, White, & Blue. Red and blue used mostly for accents/emphasis.

The main/index page's purpose is to, as best possible, convey the idea of SEM campaign management with supporting websites being their best option for internet marketing!
The secondary page is just a slightly modified layout where details can be explained.

Target Market(s)

Dentists who practice Dental Sleep Medicine (see www.pqwrl.org)

Industry/Entity Type

Marketing

Requirements
Must have
• -Sign-up form for the generation of leads... Simple script that sends E-mail is fine... Doctor's Name, Business Name, Business Address, E-mail address, phone #.

-Graphics that will clearly describe the services being provided.

```html
<!DOCTYPE html>
<html lang="en">
<head>
<meta charset="utf-8">
<title>QHOP LLC – Quiet Harbor Outreach Partners</title>
<link href="https://fonts.googleapis.com/css2?family=Roboto+Condensed:wght@300;400&family=Source+Sans+3:wght@400;600;700&display=swap" rel="stylesheet">
<style>
:root{
  --page:#f1f1f1;
  --brand-red:#b3242f;
  --brand-blue:#3b4d98;
  --nav-top:#5d6fb2;
  --nav-bottom:#3b4b8e;
  --band:#6d79ad;
  --card:#dedede;
  --field:#f2f2f2;
  --field-line:#d4d4d4;
  --ink:#2b2b2b;
  --muted:#555;
  --white:#ffffff;
  --btn-blue:#6f79ad;
}
*{box-sizing:border-box;margin:0;padding:0}
html,body{width:1200px;height:1068px;overflow:hidden}
body{background:var(--page);font-family:"Source Sans 3",sans-serif;color:var(--ink);position:relative;border-top:2px solid var(--band)}
.abs{position:absolute}
.heading{font-family:"Roboto Condensed",sans-serif;font-weight:400;color:var(--brand-blue)}

/* header */
.brand{left:162px;top:30px;display:flex;align-items:center;gap:10px}
.brand-mark{width:42px;height:42px;border-radius:50%;background:var(--brand-blue)}
.brand-name{font-weight:700;font-size:38px;line-height:1;color:var(--brand-red);letter-spacing:.5px}
.brand-tag{left:162px;top:76px;font-weight:700;font-size:12.5px;color:var(--brand-red)}
.search{left:895px;top:17px;width:143px;height:24px;background:#e8e8e8;border-radius:3px;font-size:11px;color:#666;padding:4px 9px;display:flex;justify-content:space-between;align-items:center}
.nav{left:439px;top:58px;width:599px;height:32px;border-radius:3px;background:linear-gradient(var(--nav-top),var(--nav-bottom));display:flex;box-shadow:0 2px 2px rgba(0,0,0,.25)}
.nav a{color:var(--white);font-size:11px;text-decoration:none;display:flex;align-items:center;justify-content:center;border-right:1px solid #2e3b74}
.nav a:last-child{border-right:0}

/* main panel */
.panel{left:164px;top:117px;width:873px;height:817px;background:#f3f3f3;border-radius:3px;box-shadow:0 0 6px rgba(0,0,0,.25);z-index:2}
.hero-photo{left:12px;top:16px;width:602px;height:270px;background:linear-gradient(120deg,#c7b8a5,#e6e1da 45%,#f4f2ef 70%,#a9a29a);box-shadow:0 8px 8px -4px rgba(0,0,0,.45)}
.hero-copy{left:602px;top:16px;width:259px;height:270px;background:var(--white);border:1px solid #d6d6d6;border-left:0;border-radius:0 3px 3px 0;padding:40px 16px 0 22px}
.hero-copy h1{font-size:27px;line-height:31px;margin-bottom:8px}
.hero-copy p{font-size:11.5px;line-height:16.6px;color:var(--muted)}
.dots{position:absolute;left:78px;top:236px;display:flex;gap:4px}
.dots span{width:13px;height:13px;background:#000}
.dots span.on{background:#6f79ad;border:2px solid #000}

.section-title{font-size:20px;top:308px}
.card{top:332px;height:217px;background:var(--card);border-radius:3px}
.card-photo{background:linear-gradient(#e9edf2,#cfd6de);box-shadow:0 2px 4px rgba(0,0,0,.3)}
.card p{font-size:11px;line-height:16.6px;color:var(--ink)}
.more{background:linear-gradient(#444,#000);color:var(--white);font-family:"Roboto Condensed",sans-serif;font-size:15px;border-radius:3px;display:flex;align-items:center;justify-content:center;width:48px;height:22px}

.testimonial{display:flex;gap:12px;padding:0 10px;height:68px;align-items:center;border-bottom:1px solid #c6c6c6}
.testimonial:last-child{border-bottom:0}
.avatar{width:41px;height:48px;flex:none;background:linear-gradient(#e4e4e4,#8b8f99)}

/* forms */
.field{width:236px;height:28px;background:var(--field);border:1px solid var(--field-line);border-radius:3px;font-size:11px;padding:7px 9px;color:#333}
.btn{background:var(--btn-blue);color:var(--white);font-family:"Roboto Condensed",sans-serif;font-size:15px;border-radius:3px;display:flex;align-items:center;justify-content:center;width:74px;height:27px}
.news-box{left:569px;top:608px;width:288px;height:189px;background:var(--white);border:1px solid #d8d8d8;border-radius:3px}
.news-box label{position:absolute;font-size:11px;color:#333}
.news-box .input{position:absolute;width:259px;height:28px;background:var(--field);border:1px solid var(--field-line);border-radius:4px}

/* footer */
.band{left:0;top:906px;width:1200px;height:162px;background:var(--band)}
.follow{left:163px;top:966px;font-size:12px;color:var(--white)}
.social{left:163px;top:995px;display:flex;gap:6px}
.social span{width:28px;height:28px;border-radius:4px;background:#eef0f7}
.foot-links{right:164px;top:974px;font-size:12px;color:var(--white);word-spacing:2px}
.copy{right:164px;top:996px;font-size:12px;color:var(--white)}
</style>
</head>
<body>
<header>
  <div class="abs brand"><span class="brand-mark"></span><span class="brand-name">QHOP LLC</span></div>
  <div class="abs brand-tag">Quiet Harbor Outreach Partners</div>
  <div class="abs search">search
    <svg width="12" height="12" viewBox="0 0 12 12"><circle cx="5" cy="5" r="3.5" fill="none" stroke="#777" stroke-width="1.4"/><line x1="7.5" y1="7.5" x2="11" y2="11" stroke="#777" stroke-width="1.8"/></svg>
  </div>
  <nav class="abs nav">
    <a style="width:106px">Home</a><a style="width:125px">About Us</a><a style="width:119px">Services</a><a style="width:124px">Our Blog</a><a style="width:125px">Contact Us</a>
  </nav>
</header>

<main class="abs panel">
  <div class="abs hero-photo" role="img" aria-label="Photo of a woman sleeping peacefully in bed"></div>
  <div class="abs hero-copy">
    <h1 class="heading">The trusted resource for everything sleep</h1>
    <p>Lorem Ipsum is simply dummy text of the printing and typesetting industry. Lorem Ipsum has been the industry's standard dummy text ever since the 1500s,</p>
    <div class="dots"><span></span><span class="on"></span><span></span><span></span><span></span></div>
  </div>

  <h2 class="abs heading section-title" style="left:12px">About Us</h2>
  <section class="abs card" style="left:12px;width:213px">
    <div class="abs card-photo" role="img" aria-label="Photo of a team of medical staff" style="left:11px;top:18px;width:186px;height:81px"></div>
    <p class="abs" style="left:15px;top:112px;width:190px">Lorem Ipsum is simply dummy text of the printing and typesetting industry. Lorem Ipsum has been the industry's standard dummy text ever since the 1500s,</p>
    <span class="abs more" style="left:154px;top:195px">more</span>
  </section>

  <h2 class="abs heading section-title" style="left:238px">Testimonial</h2>
  <section class="abs card" style="left:238px;width:213px;padding-top:0">
    <div class="testimonial"><div class="avatar" role="img" aria-label="Portrait of a client"></div><p>Lorem Ipsum is simply dummy text of the printing and typesetting industry.</p></div>
    <div class="testimonial"><div class="avatar" role="img" aria-label="Portrait of two clients"></div><p>Lorem Ipsum is simply dummy text of the printing and typesetting industry.</p></div>
    <div class="testimonial"><div class="avatar" role="img" aria-label="Portrait of a client"></div><p>Lorem Ipsum is simply dummy text of the printing and typesetting industry.</p></div>
  </section>

  <h2 class="abs heading section-title" style="left:467px">Services</h2>
  <section class="abs card" style="left:467px;width:394px">
    <p class="abs" style="left:18px;top:29px;width:180px;text-align:justify">Lorem Ipsum is simply dummy text of the printing and typesetting industry. Lorem Ipsum has been the industry's standard dummy text ever since the 1500s, when an unknown printer took a galley of type and scrambled it to make a type specimen book. It has survived not only five centuries...</p>
    <div class="abs card-photo" role="img" aria-label="Photo of a team of medical staff" style="left:223px;top:31px;width:171px;height:134px"></div>
    <span class="abs more" style="left:18px;top:174px">more</span>
  </section>

  <h2 class="abs heading section-title" style="left:15px;top:577px">Quick Contact</h2>
  <form>
    <div class="abs field" style="left:15px;top:611px">Doctor's Name</div>
    <div class="abs field" style="left:15px;top:647px">Business Name</div>
    <div class="abs field" style="left:15px;top:684px">Business Address</div>
    <div class="abs field" style="left:15px;top:721px">E-mail address</div>
    <div class="abs field" style="left:15px;top:758px">Phone No</div>
    <div class="abs field" style="left:264px;top:609px;width:274px;height:144px;padding:11px 14px">Message</div>
    <span class="abs btn" style="left:463px;top:764px">Submit</span>
  </form>

  <h2 class="abs heading section-title" style="left:568px;top:578px">Subscribe Our Newsletter</h2>
  <div class="abs news-box">
    <label style="left:18px;top:17px">Enter the your name</label>
    <div class="input" style="left:17px;top:35px"></div>
    <label style="left:16px;top:75px">Enter the your Email id</label>
    <div class="input" style="left:14px;top:93px"></div>
    <span class="abs btn" style="left:174px;top:134px">Submit</span>
  </div>
</main>

<footer>
  <div class="abs band"></div>
  <div class="abs follow">Follow Us on</div>
  <div class="abs social"><span></span><span></span><span></span><span></span></div>
  <div class="abs foot-links">Home &nbsp;| &nbsp;About Us &nbsp;| &nbsp;Services &nbsp;| &nbsp;Our Blog &nbsp;| &nbsp;Contact Us</div>
  <div class="abs copy">Copyrights @ 2012 All Rights Reserved</div>
</footer>
</body>
</html>
```